Brochure Projecct

I need a brochure created for my company, which will be sent to customers via email in PDF format. I have uploaded the company logo with this project, which I want incorporated in the design.

Designers should view the company website at www.brightcounselhub.com. I want the brochure to compliment the website (i.e., very clean design). I would also like pictures added to the brochure to make the design visually stunning.

In terms of content, I need four pages in the brochure to add four separate sections of content (one section per page). The four sections of content will be as follows (1) Search Engine Optimization Benefits (2) Increased Client Retention (3) Showcase Your Law Firm (4) Maximize Your Online ROI (5) Pricing Plans. I will give the content to the winning designer to add to the project. Each individual content section will have four subsection titles after which content of approximately 100 to 200 words will appear.

Designers can decide if other pages should be added to the brochure (i.e., a "cover page" that would have little content, but be visually appealing like the cover of a book - - - a "back page" that may just have the logo, contact information, etc).

My company address and email address should be prominently featured through every page (address: 7315 West Maple Ridge Avenue, Suite 1400, Scottsdale, Arizona 85377; email: sales@brightcounselhub.com).

Industry/Entity Type

It Company

Requirements
Must have
• Clean look but visually stunning incorporating the design of the website at brightcounselhub.com as well as the logo. Also, room for content as set forth in the description of this project.

```html
<!DOCTYPE html>
<html lang="en">
<head>
<meta charset="utf-8">
<title>Bright Counsel Hub Brochure Spreads</title>
<link rel="stylesheet" href="https://fonts.googleapis.com/css2?family=Lato:ital,wght@0,400;0,700;1,400;1,700&display=swap">
<style>
  :root {
    --sky: #5fb6e9;
    --sky-soft: #7cc6f0;
    --panel-glass: rgba(255, 255, 255, 0.38);
    --panel-core: rgba(170, 190, 215, 0.75);
    --divider: #2c4c74;
    --ink: #1d1d1d;
    --white: #ffffff;
    --url-bg: #b9def4;
    --url-chip: #5a73b8;
    --strip: #d6d6d6;
    --frame: #9aa3ad;
    --brand: #2f6fa3;
    --chart-bar: #4c8fd0;
    --chart-arrow: #2a3f86;
  }
  * { margin: 0; padding: 0; box-sizing: border-box; }
  html, body { width: 1200px; height: 423px; overflow: hidden; background: var(--white); }
  body { font-family: "Lato", sans-serif; position: relative; }

  .spread { position: absolute; top: 0; width: 592px; height: 423px; background: var(--white); overflow: hidden; }
  .spread--seo { left: 0; }
  .spread--retention { left: 608px; }

  .hero { position: absolute; left: 0; top: 0; width: 592px; height: 327px; background: var(--sky); }
  .title-panel { position: absolute; left: 108px; top: 0; width: 379px; height: 115px; background: var(--panel-glass); }
  .title-panel__core { position: absolute; left: 46px; top: 0; width: 216px; height: 115px; background: var(--panel-core); }
  .section-title { position: absolute; left: 108px; top: 96px; width: 379px; text-align: center; font-size: 15px; color: var(--ink); font-weight: 400; }
  .section-title strong { color: var(--white); font-weight: 700; }
  .spread--retention .section-title { left: 80px; width: 379px; }

  .copy { position: absolute; left: 137px; top: 133px; width: 455px; height: 178px; background: var(--sky-soft); display: flex; }
  .copy__column { flex: 1; padding: 6px 4px 0; border-right: 1.5px solid var(--divider); color: var(--white); font-size: 8.6px; line-height: 11.6px; text-align: justify; overflow: hidden; }
  .copy__column:last-child { border-right: none; }

  .visual-frame { position: absolute; left: 7px; top: 157px; width: 121px; height: 154px; border: 1px solid rgba(255,255,255,0.8); }
  .visual { position: absolute; left: 8px; top: 12px; width: 110px; height: 124px; }
  .visual--seo { background: linear-gradient(90deg, #f4f4f4 0%, #8a8d92 55%, #3e4249 100%); }
  .visual--chart { background: var(--white); }

  .website { position: absolute; left: 0; top: 341px; width: 228px; height: 41px; background: var(--url-bg); border: 1px solid #8fb6d2; display: flex; align-items: center; padding-left: 5px; font-size: 11px; font-style: italic; color: var(--ink); }
  .website__url { margin-left: 3px; font-style: normal; font-weight: 700; font-size: 13px; color: var(--white); background: var(--url-chip); padding: 1px 2px; border: 1px solid #33477d; }

  .brand-box { position: absolute; left: 349px; top: 331px; width: 243px; height: 74px; border: 1px solid var(--frame); background: var(--white); display: flex; align-items: center; justify-content: center; gap: 8px; }
  .brand-box__dot { width: 16px; height: 16px; border-radius: 50%; background: var(--brand); }
  .brand-box__name { font-size: 20px; font-weight: 700; color: var(--brand); }

  .contact-strip { position: absolute; left: 0; top: 407px; width: 592px; height: 16px; background: var(--strip); font-size: 10.6px; line-height: 16px; font-weight: 700; font-style: italic; color: var(--ink); white-space: nowrap; overflow: hidden; padding-left: 3px; letter-spacing: -0.1px; }
</style>
</head>
<body>

<section class="spread spread--seo">
  <div class="hero">
    <div class="title-panel"><div class="title-panel__core"></div></div>
    <h2 class="section-title"><strong>Search Engine Optimization</strong> Benefits</h2>
    <div class="copy">
      <p class="copy__column">Abcd efg hijklm no pqr stuv wxy z. Abcd efg hijklm no pqr stuv wxy z. Abcd efg hijklm no pqr stuv wxy z. Abcd efg hijklm no pqr stuv wxy z. Abcd efg hijklm no pqr stuv wxy z. Abcd efg hijklm no pqr stuv wxy z. Abcd efg hijklm no pqr stuv wxy z. Abcd efg hijklm no pqr stuv wxy z. Abcd efg hijklm no pqr stuv wxy z. Abcd efg hijklm no pqr stuv wxy z. Abcd efg</p>
      <p class="copy__column">Abcd efg hijklm no pqr stuv wxy z. Abcd efg hijklm no pqr stuv wxy z. Abcd efg hijklm no pqr stuv wxy z. Abcd efg hijklm no pqr stuv wxy z. Abcd efg hijklm no pqr stuv wxy z. Abcd efg hijklm no pqr stuv wxy z. Abcd efg hijklm no pqr stuv wxy z. Abcd efg hijklm no pqr stuv wxy z. Abcd efg hijklm no pqr stuv wxy z. Abcd efg hijklm no pqr stuv wxy z. Abcd efg</p>
      <p class="copy__column">Abcd efg hijklm no pqr stuv wxy z. Abcd efg hijklm no pqr stuv wxy z. Abcd efg hijklm no pqr stuv wxy z. Abcd efg hijklm no pqr stuv wxy z. Abcd efg hijklm no pqr stuv wxy z. Abcd efg hijklm no pqr stuv wxy z. Abcd efg hijklm no pqr stuv wxy z. Abcd efg hijklm no pqr stuv wxy z. Abcd efg hijklm no pqr stuv wxy z. Abcd efg hijklm no pqr stuv wxy z. Abcd efg</p>
      <p class="copy__column">Abcd efg hijklm no pqr stuv wxy z. Abcd efg hijklm no pqr stuv wxy z. Abcd efg hijklm no pqr stuv wxy z. Abcd efg hijklm no pqr stuv wxy z. Abcd efg hijklm no pqr stuv wxy z. Abcd efg hijklm no pqr stuv wxy z. Abcd efg hijklm no pqr stuv wxy z. Abcd efg hijklm no pqr stuv wxy z. Abcd efg hijklm no pqr stuv wxy z. Abcd efg hijklm no pqr stuv wxy z. Abcd efg</p>
    </div>
    <div class="visual-frame">
      <div class="visual visual--seo" role="img" aria-label="Photo of a businessman touching a screen labelled search engine optimization"></div>
    </div>
  </div>
  <div class="website">Website: <span class="website__url">www.brightcounselhub.com</span></div>
  <div class="brand-box"><span class="brand-box__dot"></span><span class="brand-box__name">Bright Counsel Hub</span></div>
  <p class="contact-strip">7315 West Maple Ridge Avenue, Suite 1400, Scottsdale, Arizona 85377 email: sales@brightcounselhub.com</p>
</section>

<section class="spread spread--retention">
  <div class="hero">
    <div class="title-panel"><div class="title-panel__core"></div></div>
    <h2 class="section-title">Increased client <strong>Retention</strong></h2>
    <div class="copy">
      <p class="copy__column">Abcd efg hijklm no pqr stuv wxy z. Abcd efg hijklm no pqr stuv wxy z. Abcd efg hijklm no pqr stuv wxy z. Abcd efg hijklm no pqr stuv wxy z. Abcd efg hijklm no pqr stuv wxy z. Abcd efg hijklm no pqr stuv wxy z. Abcd efg hijklm no pqr stuv wxy z. Abcd efg hijklm no pqr stuv wxy z. Abcd efg hijklm no pqr stuv wxy z. Abcd efg hijklm no pqr stuv wxy z. Abcd efg</p>
      <p class="copy__column">Abcd efg hijklm no pqr stuv wxy z. Abcd efg hijklm no pqr stuv wxy z. Abcd efg hijklm no pqr stuv wxy z. Abcd efg hijklm no pqr stuv wxy z. Abcd efg hijklm no pqr stuv wxy z. Abcd efg hijklm no pqr stuv wxy z. Abcd efg hijklm no pqr stuv wxy z. Abcd efg hijklm no pqr stuv wxy z. Abcd efg hijklm no pqr stuv wxy z. Abcd efg hijklm no pqr stuv wxy z. Abcd efg</p>
      <p class="copy__column">Abcd efg hijklm no pqr stuv wxy z. Abcd efg hijklm no pqr stuv wxy z. Abcd efg hijklm no pqr stuv wxy z. Abcd efg hijklm no pqr stuv wxy z. Abcd efg hijklm no pqr stuv wxy z. Abcd efg hijklm no pqr stuv wxy z. Abcd efg hijklm no pqr stuv wxy z. Abcd efg hijklm no pqr stuv wxy z. Abcd efg hijklm no pqr stuv wxy z. Abcd efg hijklm no pqr stuv wxy z. Abcd efg</p>
      <p class="copy__column">Abcd efg hijklm no pqr stuv wxy z. Abcd efg hijklm no pqr stuv wxy z. Abcd efg hijklm no pqr stuv wxy z. Abcd efg hijklm no pqr stuv wxy z. Abcd efg hijklm no pqr stuv wxy z. Abcd efg hijklm no pqr stuv wxy z. Abcd efg hijklm no pqr stuv wxy z. Abcd efg hijklm no pqr stuv wxy z. Abcd efg hijklm no pqr stuv wxy z. Abcd efg hijklm no pqr stuv wxy z. Abcd efg</p>
    </div>
    <div class="visual-frame">
      <svg class="visual visual--chart" viewBox="0 0 110 124" role="img" aria-label="Rising bar chart with an upward arrow">
        <rect width="110" height="124" fill="#ffffff"/>
        <g fill="var(--chart-bar)">
          <rect x="10" y="100" width="8" height="10"/>
          <rect x="22" y="96" width="8" height="14"/>
          <rect x="34" y="91" width="8" height="19"/>
          <rect x="46" y="85" width="8" height="25"/>
          <rect x="58" y="78" width="8" height="32"/>
          <rect x="70" y="70" width="8" height="40"/>
          <rect x="82" y="60" width="8" height="50"/>
        </g>
        <path d="M8 96 Q50 88 84 48" fill="none" stroke="var(--chart-arrow)" stroke-width="4"/>
        <path d="M76 44 L94 36 L90 56 Z" fill="var(--chart-arrow)"/>
      </svg>
    </div>
  </div>
  <div class="website">Website: <span class="website__url">www.brightcounselhub.com</span></div>
  <div class="brand-box"><span class="brand-box__dot"></span><span class="brand-box__name">Bright Counsel Hub</span></div>
  <p class="contact-strip">7315 West Maple Ridge Avenue, Suite 1400, Scottsdale, Arizona 85377 email: sales@brightcounselhub.com</p>
</section>

</body>
</html>
```